Catalog copying current designs, web designs and copywrite.

I am looking for someone to recreate a draft catalog using the same design process.

My entire brief with the photo samples and icons would not fit in here. They are in the google docs folder as below:

https://share.plovimbox.net/folders/7hQwRk2mZaXe9TnB4LpYcVd3sUfGj6K?mode=view

```html
<!DOCTYPE html>
<html lang="en">
<head>
<meta charset="utf-8">
<title>Northgate Staffing – Catalogue Spread</title>
<link href="https://fonts.googleapis.com/css2?family=Roboto:wght@300;400;500;700;900&display=swap" rel="stylesheet">
<style>
  :root {
    --backdrop: #9a9a9a;
    --page: #e9eaeb;
    --page-light: #f4f5f5;
    --crimson: #8b1a22;
    --ink: #4a4a4a;
    --label: #555555;
    --white: #ffffff;
    --folio: #9a9a9a;
  }
  * { margin: 0; padding: 0; box-sizing: border-box; }
  html, body { width: 1200px; height: 1000px; overflow: hidden; }
  body {
    position: relative;
    background: var(--backdrop);
    font-family: "Roboto", Arial, sans-serif;
  }
  .page {
    position: absolute;
    top: 80px;
    width: 594px;
    height: 840px;
    overflow: hidden;
    background: linear-gradient(160deg, var(--page-light) 0%, var(--page) 45%, #dfe0e1 100%);
  }
  .page--process { left: 3px; }
  .page--positions { left: 603px; }

  .brand {
    position: absolute;
    top: 44px;
    left: 42px;
    font-size: 26px;
    font-weight: 500;
    color: var(--ink);
    letter-spacing: 0.3px;
  }

  .page-title {
    position: absolute;
    font-weight: 300;
    font-size: 36px;
    line-height: 44px;
    color: var(--crimson);
    text-transform: uppercase;
    letter-spacing: 0.3px;
  }
  .page--process .page-title { right: 49px; top: 140px; text-align: right; }
  .page--positions .page-title { left: 42px; top: 132px; }

  .intro {
    position: absolute;
    right: 49px;
    top: 233px;
    width: 232px;
    text-align: right;
    font-size: 11px;
    font-weight: 300;
    line-height: 18px;
    color: var(--ink);
  }
  .subtitle {
    position: absolute;
    left: 46px;
    top: 179px;
    font-size: 12px;
    font-weight: 300;
    color: var(--ink);
    letter-spacing: 0.3px;
  }

  .red-field { position: absolute; left: 0; top: 0; width: 594px; height: 840px; }

  .snippet {
    position: absolute;
    left: 47px;
    top: 306px;
    color: var(--white);
    font-weight: 300;
    font-size: 22px;
    line-height: 29px;
    text-transform: uppercase;
  }
  .step {
    position: absolute;
    width: 170px;
    margin-left: -85px;
    text-align: center;
    color: var(--white);
  }
  .step__number { font-size: 32px; font-weight: 900; line-height: 36px; }
  .step__text { font-size: 13px; line-height: 17px; margin-top: 4px; }

  .folio-corner { position: absolute; right: 0; bottom: 0; }
  .folio {
    position: absolute;
    right: 22px;
    bottom: 17px;
    font-size: 12px;
    color: var(--folio);
  }

  .positions {
    position: absolute;
    left: 25px;
    top: 222px;
    display: grid;
    grid-template-columns: repeat(4, 142px);
    row-gap: 26px;
  }
  .position {
    display: flex;
    flex-direction: column;
    align-items: center;
    height: 104px;
  }
  .position__icon {
    width: 48px; height: 52px;
    border-radius: 6px;
    background: var(--crimson);
    opacity: 0.85;
  }
  .position__label {
    margin-top: 20px;
    font-size: 12px;
    font-weight: 700;
    line-height: 15px;
    color: var(--label);
    text-align: center;
    text-transform: uppercase;
  }
  .photo-collage { position: absolute; left: 0; top: 0; }
</style>
</head>
<body>

  <section class="page page--process">
    <svg class="red-field" viewBox="0 0 594 840" aria-hidden="true">
      <defs>
        <linearGradient id="redFill" x1="0" y1="0" x2="1" y2="1">
          <stop offset="0" stop-color="#6a121a"/>
          <stop offset="0.5" stop-color="#7e1820"/>
          <stop offset="1" stop-color="#6b131b"/>
        </linearGradient>
      </defs>
      <polygon points="0,192 162,196 302,350 430,460 594,545 594,760 488,840 0,840" fill="url(#redFill)"/>
    </svg>

    <div class="brand">Northgate Staffing</div>

    <h1 class="page-title">Our Recruitment<br>Process</h1>
    <p class="intro">Our job is to simplify difficulties of recruitment so you can focus on what you do best, it is vital to understand your needs so we can find you the newest addition to your team.</p>

    <h2 class="snippet">Here’s a<br>snippet of<br>our process:</h2>

    <div class="step" style="left:107px; top:455px;"><div class="step__number">1.</div><div class="step__text">Understanding<br>what you want</div></div>
    <div class="step" style="left:272px; top:505px;"><div class="step__number">2.</div><div class="step__text">Screen through<br>candidates</div></div>
    <div class="step" style="left:437px; top:555px;"><div class="step__number">3.</div><div class="step__text">Interview the most<br>eligible candidates</div></div>
    <div class="step" style="left:107px; top:596px;"><div class="step__number">4.</div><div class="step__text">Perform reference<br>checks</div></div>
    <div class="step" style="left:272px; top:646px;"><div class="step__number">5.</div><div class="step__text">Arrange interview</div></div>
    <div class="step" style="left:437px; top:697px;"><div class="step__number">6.</div><div class="step__text">Place the Candidate</div></div>

    <svg class="folio-corner" width="110" height="80" viewBox="0 0 110 80" aria-hidden="true">
      <polygon points="110,0 110,80 0,80" fill="#f4f5f5"/>
    </svg>
    <span class="folio">7</span>
  </section>

  <section class="page page--positions">
    <div class="brand">Northgate Staffing</div>

    <h1 class="page-title">Positions We Provide</h1>
    <p class="subtitle">(BUT NOT LIMITED TO)</p>

    <div class="positions">
      <div class="position"><div class="position__icon" role="img" aria-label="Construction manager figure icon"></div><div class="position__label">Construction<br>Manager</div></div>
      <div class="position"><div class="position__icon" role="img" aria-label="Project manager figure icon"></div><div class="position__label">Project<br>Manager</div></div>
      <div class="position"><div class="position__icon" role="img" aria-label="Site manager figure icon"></div><div class="position__label">Site<br>Manager</div></div>
      <div class="position"><div class="position__icon" role="img" aria-label="Foreman in hard hat icon"></div><div class="position__label">Foreman</div></div>
      <div class="position"><div class="position__icon" role="img" aria-label="Estimator document with magnifier icon"></div><div class="position__label">Estimator</div></div>
      <div class="position"><div class="position__icon" role="img" aria-label="Contracts administrator document icon"></div><div class="position__label">Contracts<br>Administrator</div></div>
      <div class="position"><div class="position__icon" role="img" aria-label="Leading hand worker icon"></div><div class="position__label">Leading<br>Hand</div></div>
      <div class="position"><div class="position__icon" role="img" aria-label="Cadet in hard hat icon"></div><div class="position__label">Cadet</div></div>
    </div>

    <svg class="photo-collage" width="594" height="840" viewBox="0 0 594 840">
      <defs>
        <linearGradient id="photoGrey" x1="0" y1="0" x2="1" y2="1">
          <stop offset="0" stop-color="#d8d8d8"/>
          <stop offset="0.5" stop-color="#a9a9a9"/>
          <stop offset="1" stop-color="#cfcfcf"/>
        </linearGradient>
        <linearGradient id="photoRed" x1="0" y1="0" x2="0" y2="1">
          <stop offset="0" stop-color="#c4705e"/>
          <stop offset="1" stop-color="#8f3a2c"/>
        </linearGradient>
      </defs>
      <g stroke="#ffffff" stroke-width="1" fill="none" opacity="0.9">
        <line x1="0" y1="640" x2="350" y2="445"/>
        <line x1="0" y1="690" x2="390" y2="470"/>
        <line x1="0" y1="710" x2="250" y2="840"/>
        <line x1="345" y1="840" x2="390" y2="470"/>
      </g>
      <polygon points="0,498 397,498 200,835" fill="url(#photoGrey)" role="img" aria-label="Photo of two site workers in hard hats reviewing plans"/>
      <polygon points="349,548 519,548 405,700" fill="url(#photoRed)" role="img" aria-label="Red-toned photo of a construction site interior"/>
      <polygon points="279,787 452,787 362,635" fill="url(#photoRed)" role="img" aria-label="Red-toned photo of workers on site"/>
    </svg>

    <svg class="folio-corner" width="110" height="80" viewBox="0 0 110 80" aria-hidden="true">
      <polygon points="110,0 110,80 0,80" fill="#f4f5f5"/>
    </svg>
    <span class="folio">7</span>
  </section>

</body>
</html>
```